Brightmoor Learning Data Dashboard

Brightmoor Learning is a leading provider of digital curriculum and online courses to increase educational opportunities and achievement to students in grades K-12. Teachers and students access all course materials online.

School districts need greater visibility into the rate in which students are progressing through their courses, so school staff can better support students to complete courses at the required rate to keep them on track for graduation.
This can be accomplished by allowing school administrators to view a data dashboard and pull an on-demand report and see progress for a specified date range, relative to overall progress.

Within a specified date range, school administrators want to know if the student made more or less progress than in the period prior to the first date in the range.
School administrators also want to know if students are ahead or behind where they should be after the second date in the range.

Industry/Entity Type

Digital

```html
<!DOCTYPE html>
<html lang="en">
<head>
<meta charset="utf-8">
<title>Brightmoor Learning – Time Based Performance Report</title>
<link href="https://fonts.googleapis.com/css2?family=Open+Sans:wght@400;600&display=swap" rel="stylesheet">
<style>
:root{
  --navy:#1f1650;
  --navy-line:#332a66;
  --head:#241b54;
  --head-mid:#31276a;
  --head-light:#4a3e93;
  --nav-text:#9d93d6;
  --bar:#d6d6d6;
  --page:#e4e4e4;
  --white:#ffffff;
  --ink:#333333;
  --muted:#555555;
  --clear:#cfcfcf;
  --red:#d0021b;
  --green:#3f9a26;
  --rule:#d2d2d2;
}
*{box-sizing:border-box;margin:0;padding:0}
html,body{width:1200px;height:461px;overflow:hidden}
body{font-family:"Open Sans",Arial,sans-serif;background:var(--page);position:relative;color:var(--ink)}

.sidebar{position:absolute;left:0;top:0;width:134px;height:461px;background:var(--navy)}
.brand{height:72px;display:flex;align-items:center;justify-content:center;gap:6px;color:var(--white);font-size:12px;font-weight:600;line-height:1.1}
.brand-dot{width:10px;height:10px;border-radius:50%;background:var(--white);flex:none}
.nav{list-style:none}
.nav li{height:41px;border-bottom:1px solid var(--navy-line);display:flex;align-items:center;padding-left:11px;gap:9px;font-size:10.5px;color:var(--nav-text);letter-spacing:.2px}
.nav li.active{color:var(--white);background:#1c1449}
.nav svg{width:11px;height:11px;fill:currentColor;flex:none}

.topbar{position:absolute;left:134px;top:0;width:1066px;height:72px;background:var(--bar)}
.field{position:absolute;top:29px;height:26px;background:var(--white);display:flex;align-items:center;font-size:7px;color:var(--muted);padding-left:10px}
.field .clear{position:absolute;right:0;top:0;width:19px;height:26px;background:var(--clear);display:flex;align-items:center;justify-content:center}
.field .clear svg{width:8px;height:8px}
.field .caret{position:absolute;right:25px;top:11px;border-left:3px solid transparent;border-right:3px solid transparent;border-top:4px solid #666}
.field .cal{position:absolute;right:25px;top:8px;width:9px;height:9px}
.label{position:absolute;top:15px;font-size:9px;color:#444}
.radio{display:inline-flex;align-items:center;gap:3px;margin-right:9px}
.radio i{width:8px;height:8px;border-radius:50%;border:1px solid #888;background:var(--white);display:inline-block}
.radio i.on{border:2.5px solid #222}
.download{position:absolute;left:784px;top:29px;width:88px;height:26px;background:var(--head);color:var(--white);font-size:8px;display:flex;align-items:center;justify-content:center;gap:5px;border-radius:2px}
.download svg{width:7px;height:8px;fill:none;stroke:var(--white);stroke-width:1}
.user{position:absolute;right:44px;top:26px;text-align:right;color:#222;line-height:1.15;white-space:nowrap}
.user small{display:block;font-size:6.5px}
.user span{font-size:9.5px}
.avatar{position:absolute;right:12px;top:22px;width:26px;height:26px;border-radius:50%;background:linear-gradient(#8a7b6e,#4d4540)}

.title{position:absolute;left:144px;top:80px;font-size:22px;font-weight:600;color:var(--head)}

.report{position:absolute;left:144px;top:112px;width:1046px;border-collapse:collapse;table-layout:fixed;font-size:7px}
.report th{background:var(--head);color:var(--white);font-weight:400;text-align:left;vertical-align:top;padding:4px 4px 4px 7px;font-size:8.2px;line-height:1.3;border-right:1px solid #3d3378}
.report th.group{text-align:center;height:20px;padding:4px}
.report th.sub{background:var(--head-mid);text-align:center;height:20px;padding:4px}
.report th.metric{background:var(--head-light);text-align:center;height:21px;padding:5px 4px 4px}
.report td{background:var(--white);height:42px;padding:0 2px 0 7px;vertical-align:middle;border-right:1px solid var(--rule);border-bottom:1px solid var(--rule);line-height:1.45}
.report td.c{text-align:center;padding:0 2px}
.nowrap{white-space:nowrap}
.bad{color:var(--red)}
.good{color:var(--green)}
.trend svg{width:8px;height:8px;fill:#222}

.footer{position:absolute;left:134px;width:1066px;top:436px;text-align:center;font-size:7.5px;color:#333}
</style>
</head>
<body>

<aside class="sidebar">
  <div class="brand"><span class="brand-dot"></span><span>Brightmoor<br>Learning</span></div>
  <ul class="nav">
    <li class="active"><svg viewBox="0 0 12 12"><path d="M6 1a5.5 5.5 0 0 0-5.5 5.5c0 1.5.6 2.8 1.5 3.8h8c.9-1 1.5-2.3 1.5-3.8A5.5 5.5 0 0 0 6 1zm.6 6.4a1 1 0 1 1-1.2-.9l2.4-3 .5.3z"/></svg>DASHBOARD</li>
    <li><svg viewBox="0 0 12 12"><circle cx="6" cy="3.5" r="2.7"/><path d="M.8 11.5c0-3 2.3-4.8 5.2-4.8s5.2 1.8 5.2 4.8z"/></svg>TEACHERS</li>
    <li><svg viewBox="0 0 12 12"><path d="M2 .5h5l3 3v8H2zM4 6h4v.8H4zm0 2h4v.8H4z"/></svg>COURSES</li>
    <li><svg viewBox="0 0 12 12"><path d="M.5 2.5h11v1L6 7 .5 3.5zm0 2.3L6 8.3l5.5-3.5v5H.5z"/></svg>MESSAGES</li>
    <li><svg viewBox="0 0 12 12"><path d="M2 .5h8.5v11H2zM1 2.5h1.5v1H1zm0 3h1.5v1H1zm0 3h1.5v1H1z"/><circle cx="6.3" cy="4.7" r="1.5" fill="#1f1650"/><path d="M3.8 9c0-1.4 1.1-2.2 2.5-2.2s2.5.8 2.5 2.2z" fill="#1f1650"/></svg>CONTACTS</li>
  </ul>
</aside>

<header class="topbar">
  <div class="label" style="left:10px">School</div>
  <div class="field" style="left:10px;width:153px">Choose a school<span class="caret"></span><span class="clear"><svg viewBox="0 0 10 10"><circle cx="5" cy="5" r="4.5" fill="#666"/><path d="M3.3 3.3l3.4 3.4M6.7 3.3L3.3 6.7" stroke="#cfcfcf" stroke-width="1.2"/></svg></span></div>

  <div class="label" style="left:179px"><span class="radio"><i class="on"></i>Observer</span><span class="radio"><i></i>Teacher</span></div>
  <div class="field" style="left:179px;width:154px">Choose a observer<span class="caret"></span><span class="clear"><svg viewBox="0 0 10 10"><circle cx="5" cy="5" r="4.5" fill="#666"/><path d="M3.3 3.3l3.4 3.4M6.7 3.3L3.3 6.7" stroke="#cfcfcf" stroke-width="1.2"/></svg></span></div>

  <div class="label" style="left:348px">Filter Date 1 :</div>
  <div class="field" style="left:348px;width:154px">2/27/18<svg class="cal" viewBox="0 0 10 10"><path d="M1 2h8v7.5H1z" fill="none" stroke="#666"/><path d="M1 2h8v2H1zM3 .5v2M7 .5v2" stroke="#666"/></svg><span class="clear"><svg viewBox="0 0 10 10"><circle cx="5" cy="5" r="4.5" fill="#666"/><path d="M3.3 3.3l3.4 3.4M6.7 3.3L3.3 6.7" stroke="#cfcfcf" stroke-width="1.2"/></svg></span></div>

  <div class="label" style="left:517px">Filter Date 2 :</div>
  <div class="field" style="left:517px;width:154px">3/6/18<svg class="cal" viewBox="0 0 10 10"><path d="M1 2h8v7.5H1z" fill="none" stroke="#666"/><path d="M1 2h8v2H1zM3 .5v2M7 .5v2" stroke="#666"/></svg><span class="clear"><svg viewBox="0 0 10 10"><circle cx="5" cy="5" r="4.5" fill="#666"/><path d="M3.3 3.3l3.4 3.4M6.7 3.3L3.3 6.7" stroke="#cfcfcf" stroke-width="1.2"/></svg></span></div>

  <div class="download"><svg viewBox="0 0 7 8"><path d="M.5.5h4l2 2v5h-6z"/><path d="M2 3.5l3 3M5 3.5l-3 3"/></svg>Download Excel</div>

  <div class="user"><small>Welcome</small><span>Dan Reyes</span></div>
  <div class="avatar" role="img" aria-label="User profile photo"></div>
</header>

<h1 class="title">Time Based Performance Report</h1>

<table class="report">
  <colgroup><col span="17" style="width:61.53px"></colgroup>
  <thead>
    <tr>
      <th rowspan="3">Student<br>Name</th>
      <th rowspan="3">Observer</th>
      <th rowspan="3">School</th>
      <th rowspan="3">Course Title</th>
      <th rowspan="3">Current<br>Grade</th>
      <th rowspan="3">Raw Score</th>
      <th rowspan="3">Course Start<br>Date</th>
      <th rowspan="3">Course End<br>Date</th>
      <th colspan="4" class="group">Percent Complete</th>
      <th rowspan="3">2/27-3/6<br>Progress<br>Actual/<br>Goal</th>
      <th rowspan="3">Status as<br>of March 6</th>
      <th rowspan="3">Completion<br>Rate / day for<br>the range</th>
      <th rowspan="3">Completion<br>Rate Change</th>
      <th rowspan="3">Last Login</th>
    </tr>
    <tr>
      <th colspan="2" class="sub">START – 2/27/18</th>
      <th colspan="2" class="sub">END – 3/6/18</th>
    </tr>
    <tr>
      <th class="metric">Actual %</th><th class="metric">Goal %</th>
      <th class="metric">Actual %</th><th class="metric">Goal %</th>
    </tr>
  </thead>
  <tbody>
    <tr><td class="nowrap">Anthony Jones</td><td>Sam Cox</td><td>Rosemont</td><td>Algebra 1A</td><td>67.3 %</td><td>70 %</td><td>2/20/18</td><td>4/24/18</td><td class="c">0%</td><td class="c">10%</td><td class="c">5%</td><td class="c">20%</td><td class="bad">5/10</td><td class="bad">5/20</td><td>.2%</td><td class="c trend"><svg viewBox="0 0 8 8"><path d="M4 0L8 4H5v4H3V4H0z"/></svg></td><td>3/6/18</td></tr>
    <tr><td>Jose Alvarez</td><td>Sam Cox</td><td>Rosemont</td><td>Biology A</td><td>74.2%</td><td>83%</td><td>2/20/18</td><td>4/24/18</td><td class="c">5%</td><td class="c">10%</td><td class="c">15%</td><td class="c">20%</td><td class="good">10/10</td><td class="bad">15/20</td><td>2.28%</td><td class="c trend"><svg viewBox="0 0 8 8"><path d="M4 0L8 4H5v4H3V4H0z"/></svg></td><td>3/6/18</td></tr>
    <tr><td>Maria Lee</td><td class="nowrap">Jema Interiano</td><td>Rosemont</td><td>US History A</td><td>82.3%</td><td>82.3%</td><td>2/20/18</td><td>4/24/18</td><td class="c">15%</td><td class="c">10%</td><td class="c">20%</td><td class="c">20%</td><td class="bad">5/10</td><td class="good">20/20</td><td>7.14%</td><td class="c trend"><svg viewBox="0 0 8 8"><path d="M4 8L8 4H5V0H3v4H0z"/></svg></td><td>3/3/18</td></tr>
    <tr><td>Marcus Smith</td><td class="nowrap">Jema Interiano</td><td>Rosemont</td><td>Algebra 1A</td><td>91.0%</td><td>95.0%</td><td>2/20/18</td><td>4/24/18</td><td class="c">9%</td><td class="c">10%</td><td class="c">11%</td><td class="c">20%</td><td class="bad">2/10</td><td class="bad">11/20</td><td>5%</td><td class="c trend"><svg viewBox="0 0 8 8"><path d="M4 0L8 4H5v4H3V4H0z"/></svg></td><td>3/3/18</td></tr>
    <tr><td class="nowrap">Juan Rodriguez</td><td>Meg Johnson</td><td>Rosemont</td><td>Language Arts<br>10 A</td><td>94.5%</td><td>94.5%</td><td>2/20/18</td><td>4/24/18</td><td class="c">11%</td><td class="c">10%</td><td class="c">28%</td><td class="c">20%</td><td class="good">17/10</td><td class="good">28/20</td><td>2.8%</td><td class="c trend"><svg viewBox="0 0 8 8"><path d="M0 4l3-3v2h2V1l3 3-3 3V5H3v2z"/></svg></td><td>3/2/18</td></tr>
    <tr><td>Jose Carlos</td><td>Meg Johnson</td><td>Rosemont</td><td>Language Arts<br>10 A</td><td>80%</td><td>85%</td><td>2/20/18</td><td>4/24/18</td><td class="c">5%</td><td class="c">10%</td><td class="c">10%</td><td class="c">20%</td><td class="bad">5/10</td><td class="bad">10/20</td><td>.3%</td><td class="c trend"><svg viewBox="0 0 8 8"><path d="M0 4l3-3v2h2V1l3 3-3 3V5H3v2z"/></svg></td><td>3/2/18</td></tr>
  </tbody>
</table>

<footer class="footer">Copyright © 2018 Brightmoor Learning. All rights reserved.</footer>

</body>
</html>
```